National Virtual CPA Firm needs post card design

Virtual CPA firm called "BRELLVO" needs a 5.5” x 8.5” post card designed to market our services to middle market mid-size american businesses. We provide Full Service Payroll (includes the processing of payroll, printing of checks and direct depositing, tax filing, and tax payments), Bookkeeping (Using their native systems, or ours), Contract CFO (with expense reduction analysis), Reporting services for business directors to make informed decisions, Capital Fundraising (Advice on seeking equity to help grow your business), and Taxes (Personal (1040), Partnership (1065), Corporate (1120, 1120S (Including Consolidated Returns)), Trust (1041) and Non-Profit (990)), including all affiliated state returns. One of our major selling points is our variety of experience, and our fast turn around times on projects.
This project specifically, I would like to highlight the bookkeeping services, but still want the tax and payroll services listed on the postcard.
I have uploaded the logo design for BRELLVO and would like a postcard that compliments the logo.
Company contact info is:
Brellvo accounting services Inc
P.O. Box 4638
Great falls, MT 59172
(800) 613-2794
Www.brellvo-example.com
Target Market(s)
Small to medium size businesses
Industry/Entity Type
Accounting
Look and feel

```html
<!DOCTYPE html>
<html lang="en">
<head>
<meta charset="utf-8">
<title>Brellvo postcard, front and back</title>
<link href="https://fonts.googleapis.com/css2?family=Open+Sans:wght@400;600;700;800&family=Bebas+Neue&family=Arimo:wght@400;700&display=swap" rel="stylesheet">
<style>
  :root{
    --ink:#231f20;
    --grey:#4a4a4a;
    --green:#3aaa35;
    --green-light:#8cc63f;
    --green-dark:#17853a;
    --yellow:#ffcb05;
    --white:#ffffff;
    --page:#e6e7e9;
  }
  *{box-sizing:border-box;margin:0;padding:0}
  html,body{width:1200px;height:900px;overflow:hidden}
  body{background:var(--page);font-family:"Open Sans",sans-serif;color:var(--ink);position:relative}

  .postcard{position:absolute;left:270px;width:660px;height:427px;background:var(--white);overflow:hidden;box-shadow:0 6px 18px rgba(0,0,0,.18)}
  .postcard--front{top:14px}
  .postcard--back{top:459px}
  .postcard__shapes{position:absolute;inset:0;width:660px;height:427px}
  .abs{position:absolute}

  .brand{display:flex;align-items:center;gap:8px}
  .brand__dot{width:20px;height:20px;border-radius:50%;background:var(--yellow)}
  .brand__name{font-weight:800;font-size:30px;letter-spacing:1px;color:var(--ink);line-height:1}

  .headline{font-weight:800;font-size:17.5px;line-height:1.15;text-transform:uppercase;color:var(--ink)}

  .service{display:flex;align-items:center;gap:10px}
  .service__icon{width:34px;height:34px;flex:none}
  .service__title{font-weight:800;font-size:14px;color:var(--green);text-transform:uppercase;line-height:1.1}
  .service__desc{font-size:10.5px;color:var(--grey);line-height:1.25}

  .tab{background:var(--green-light);color:var(--white);font-weight:800;text-transform:uppercase;border-radius:0 16px 16px 0;padding:5px 18px 5px 16px;font-size:14px}

  .benefit{display:flex;flex-direction:column;align-items:center;gap:4px;color:var(--white);font-weight:800;font-size:11px;text-transform:uppercase}
  .benefit svg{width:28px;height:28px}

  .badge{width:100px;height:100px;border-radius:50%;background:var(--yellow);border:3px solid var(--white);display:flex;align-items:center;justify-content:center;text-align:center;font-family:"Bebas Neue",sans-serif;font-size:18px;line-height:.95;color:var(--ink);box-shadow:0 2px 6px rgba(0,0,0,.25)}

  .cta__title{font-weight:800;font-size:15px;color:var(--yellow);text-transform:uppercase;white-space:nowrap}
  .cta__contact{display:flex;flex-direction:column;gap:3px;color:var(--white);font-weight:600;margin-top:6px;white-space:nowrap}
  .cta__item{display:flex;align-items:center;gap:6px}
  .cta__phone{font-size:15px}
  .cta__web{font-size:12px}
  .cta__item svg{width:13px;height:13px;flex:none}

  .list-other{display:flex;flex-direction:column;gap:5px}
  .list-other .service__icon{width:24px;height:24px}
  .list-other .service__title{font-size:11.5px;color:var(--ink);text-transform:none;font-weight:700}
  .list-other .service__desc{font-size:10px}

  .closing{color:var(--white);font-weight:800;font-size:12px;line-height:1.25;text-transform:uppercase}
  .closing__name{color:var(--yellow)}

  .indicia{border:1px solid var(--ink);font-family:"Arimo",sans-serif;font-size:9.5px;line-height:1.25;text-align:center;padding:5px 6px;width:86px;background:var(--white)}
  .indicia b{font-weight:700}
</style>
</head>
<body>

<section class="postcard postcard--front" aria-label="Postcard front">
  <svg class="postcard__shapes" viewBox="0 0 660 427">
    <defs>
      <linearGradient id="photoWarm" x1="0" y1="0" x2="1" y2="1">
        <stop offset="0" stop-color="#5f7784"/>
        <stop offset=".45" stop-color="#c9a27a"/>
        <stop offset=".75" stop-color="#f3b35a"/>
        <stop offset="1" stop-color="#8a98a4"/>
      </linearGradient>
      <linearGradient id="bandGreen" x1="0" y1="0" x2="0" y2="1">
        <stop offset="0" stop-color="#7dc242"/>
        <stop offset="1" stop-color="#17853a"/>
      </linearGradient>
    </defs>
    <path role="img" aria-label="Photo of a businessman working at a laptop with a rising growth chart overlay" d="M300,0 H660 V290 H370 Q345,150 300,0 Z" fill="url(#photoWarm)"/>
    <path d="M262,0 H300 Q360,200 392,427 H372 Q338,200 262,0 Z" fill="var(--green)"/>
    <path d="M0,362 C120,352 260,312 364,252 L392,427 H0 Z" fill="url(#bandGreen)"/>
    <path d="M370,290 H660 V427 H392 Z" fill="var(--ink)"/>
    <line x1="370" y1="290" x2="660" y2="290" stroke="#f39a2b" stroke-width="2"/>
  </svg>

  <div class="brand abs" style="left:40px;top:22px">
    <span class="brand__dot"></span><span class="brand__name">BRELLVO</span>
  </div>

  <h1 class="headline abs" style="left:40px;top:68px">Virtual and remote CPA<br>and accounting services</h1>

  <div class="abs" style="left:30px;top:122px;display:flex;flex-direction:column;gap:7px;width:280px">
    <div class="service">
      <svg class="service__icon" viewBox="0 0 36 36"><circle cx="18" cy="18" r="17" fill="var(--green-light)"/><rect x="11" y="9" width="14" height="18" rx="1" fill="none" stroke="#fff" stroke-width="1.6"/><path d="M14 14h8M14 18h8M14 22h5" stroke="#fff" stroke-width="1.4"/></svg>
      <div><div class="service__title">Bookkeeping</div><div class="service__desc">Using their native systems, or ours</div></div>
    </div>
    <div class="service">
      <svg class="service__icon" viewBox="0 0 36 36"><circle cx="18" cy="18" r="17" fill="var(--green-light)"/><rect x="10" y="9" width="13" height="17" rx="1" fill="none" stroke="#fff" stroke-width="1.6"/><ellipse cx="24" cy="24" rx="5" ry="2" fill="none" stroke="#fff" stroke-width="1.4"/><ellipse cx="24" cy="27" rx="5" ry="2" fill="none" stroke="#fff" stroke-width="1.4"/></svg>
      <div><div class="service__title">Taxes</div><div class="service__desc">(Personal (1040), Partnership (1065)</div></div>
    </div>
    <div class="service">
      <svg class="service__icon" viewBox="0 0 36 36"><circle cx="18" cy="18" r="17" fill="var(--green-light)"/><rect x="10" y="9" width="14" height="18" rx="1" fill="none" stroke="#fff" stroke-width="1.6"/><circle cx="21" cy="20" r="4" fill="none" stroke="#fff" stroke-width="1.6"/><path d="M24 23l3 3" stroke="#fff" stroke-width="1.8"/></svg>
      <div><div class="service__title">Full service payroll</div><div class="service__desc">includes the processing of payroll, printing<br>of checks and direct depositing, tax filing,<br>and tax payments</div></div>
    </div>
  </div>

  <div class="tab abs" style="left:0;top:322px;width:215px">Why choose us?</div>

  <div class="benefit abs" style="left:40px;top:360px">
    <svg viewBox="0 0 30 30" fill="none" stroke="var(--yellow)" stroke-width="1.8"><circle cx="12" cy="11" r="6"/><circle cx="21" cy="18" r="5"/><path d="M21 15v3l2 1M8 22l-2 6 6-3"/></svg>
    <span>Expirienced</span>
  </div>
  <div class="benefit abs" style="left:160px;top:350px">
    <svg viewBox="0 0 30 30" fill="none" stroke="var(--yellow)" stroke-width="1.8"><circle cx="9" cy="8" r="3"/><circle cx="15" cy="6" r="3"/><circle cx="21" cy="8" r="3"/><path d="M4 18c3-4 8-4 11-2 3-2 8-2 11 2M5 24h20"/></svg>
    <span>Professional</span>
  </div>
  <div class="benefit abs" style="left:280px;top:334px">
    <svg viewBox="0 0 30 30" fill="none" stroke="var(--yellow)" stroke-width="1.8"><circle cx="16" cy="10" r="7"/><path d="M16 6v8M14 8h3.5a1.5 1.5 0 010 3H14.5a1.5 1.5 0 000 3H18M3 24l6-3h8l8-4"/></svg>
    <span>Affordable</span>
  </div>

  <div class="badge abs" style="left:296px;top:222px">Business<br>advisors and<br>consultants</div>

  <div class="abs" style="left:404px;top:304px">
    <div class="cta__title">Shedule a free consult now</div>
    <div class="cta__contact">
      <span class="cta__item cta__phone"><svg viewBox="0 0 14 14"><circle cx="7" cy="7" r="6" fill="none" stroke="var(--yellow)" stroke-width="1.4"/><path d="M5 4l1.5 1.5-1 1 2 2 1-1L10 9l-1 1.2C7 10 4 7 3.8 5z" fill="var(--yellow)"/></svg>(800) 613-2794</span>
      <span class="cta__item cta__web"><svg viewBox="0 0 14 14"><circle cx="7" cy="7" r="6" fill="none" stroke="var(--yellow)" stroke-width="1.4"/><path d="M1 7h12M7 1c3 3 3 9 0 12M7 1c-3 3-3 9 0 12" fill="none" stroke="var(--yellow)" stroke-width="1"/></svg>BRELLVO-EXAMPLE.COM</span>
    </div>
  </div>
</section>

<section class="postcard postcard--back" aria-label="Postcard back">
  <svg class="postcard__shapes" viewBox="0 0 660 427">
    <defs>
      <linearGradient id="photoCool" x1="0" y1="0" x2="1" y2="1">
        <stop offset="0" stop-color="#1f3b5a"/>
        <stop offset=".5" stop-color="#5d7f9d"/>
        <stop offset="1" stop-color="#c9d6e2"/>
      </linearGradient>
      <linearGradient id="bandGreenBack" x1="0" y1="0" x2="1" y2="0">
        <stop offset="0" stop-color="#7dc242"/>
        <stop offset="1" stop-color="#17853a"/>
      </linearGradient>
    </defs>
    <path role="img" aria-label="Photo collage of business meetings and handshakes in hexagon frames" d="M0,0 H330 Q376,90 382,165 H0 Z" fill="url(#photoCool)"/>
    <path d="M322,0 H342 Q432,220 410,427 H392 Q412,220 322,0 Z" fill="var(--green)"/>
    <path d="M0,382 L403,345 L400,427 H0 Z" fill="url(#bandGreenBack)"/>
    <path d="M400,300 H660 V427 H398 Z" fill="var(--ink)"/>
  </svg>

  <div class="tab abs" style="left:0;top:152px;width:200px">Our other services</div>

  <div class="list-other abs" style="left:18px;top:190px;width:380px">
    <div class="service">
      <svg class="service__icon" viewBox="0 0 26 26" fill="none" stroke="var(--green)" stroke-width="1.4"><rect x="4" y="3" width="14" height="19" rx="1"/><path d="M7 8h8M7 12h8M7 16h5"/><circle cx="19" cy="19" r="4"/><path d="M17 19l1.5 1.5L21 18"/></svg>
      <div><div class="service__title">Contract CFO</div><div class="service__desc">with expense reduction analysis</div></div>
    </div>
    <div class="service">
      <svg class="service__icon" viewBox="0 0 26 26" fill="none" stroke="var(--green)" stroke-width="1.4"><rect x="4" y="3" width="16" height="20" rx="1"/><path d="M8 18v-3M12 18v-6M16 18v-9"/></svg>
      <div><div class="service__title">Reporting Services</div><div class="service__desc">for business directors to make informed decisions</div></div>
    </div>
    <div class="service">
      <svg class="service__icon" viewBox="0 0 26 26" fill="none" stroke="var(--green)" stroke-width="1.4"><circle cx="9" cy="16" r="3"/><path d="M4 24c1-3 3-4 5-4s4 1 5 4"/><rect x="12" y="3" width="11" height="8" rx="2"/><path d="M15 7h5"/></svg>
      <div><div class="service__title">Capital Fundraising</div><div class="service__desc">Advice on seeking equity to help grow your business</div></div>
    </div>
    <div class="service">
      <svg class="service__icon" viewBox="0 0 26 26" fill="none" stroke="var(--green)" stroke-width="1.4"><rect x="4" y="3" width="16" height="20" rx="1"/><path d="M7 8h10M7 17l5-5"/><circle cx="8" cy="13" r="1"/><circle cx="12" cy="17" r="1"/></svg>
      <div><div class="service__title">Taxes</div><div class="service__desc">(Personal (1040), Partnership (1065), Corporate (1120, 1120S<br>(Including Consolidated Returns))Trust (1041) and Non-Profit (990)),<br>including all affiliated state returns.</div></div>
    </div>
  </div>

  <p class="closing abs" style="left:18px;top:376px;width:380px">Contact <span class="closing__name">Brellvo</span> to discuss your accounting<br>and CPA needs, and see just how well virtual<br>services may serve you.</p>

  <div class="badge abs" style="left:350px;top:100px">Business<br>advisors and<br>consultants</div>

  <div class="brand abs" style="left:470px;top:112px">
    <span class="brand__dot" style="width:18px;height:18px"></span><span class="brand__name" style="font-size:26px">BRELLVO</span>
  </div>

  <div class="indicia abs" style="left:556px;top:16px">PRSRT STD<br>ECRWSS<br>U.S. Postage<br><b>PAID</b><br>EDDM RETAIL</div>

  <div class="abs" style="left:414px;top:312px">
    <div class="cta__title" style="font-size:14px">Shedule a free consult now</div>
    <div class="cta__contact">
      <span class="cta__item cta__phone"><svg viewBox="0 0 14 14"><circle cx="7" cy="7" r="6" fill="none" stroke="var(--yellow)" stroke-width="1.4"/><path d="M5 4l1.5 1.5-1 1 2 2 1-1L10 9l-1 1.2C7 10 4 7 3.8 5z" fill="var(--yellow)"/></svg>(800) 613-2794</span>
      <span class="cta__item cta__web"><svg viewBox="0 0 14 14"><circle cx="7" cy="7" r="6" fill="none" stroke="var(--yellow)" stroke-width="1.4"/><path d="M1 7h12M7 1c3 3 3 9 0 12M7 1c-3 3-3 9 0 12" fill="none" stroke="var(--yellow)" stroke-width="1"/></svg>BRELLVO-EXAMPLE.COM</span>
    </div>
  </div>
</section>

</body>
</html>
```